Bright Builders WA Ball Poster

To Create a Poster for the Bright Builders WA Ball 2013

Target Market(s)

Young Professional Engineers aged 18-35. Male and Female

Requirements
Must have
• All Details required for the ball. Black and white/silver theme. Some kind of engineering theme. Must have the following text:

Join us in celebrating the Annual Bright Builders of Western Australia Ball with a night of dinner and entertainment.
Saturday July 13th, 2013
Time: 7pm Arrival
Venue: Corvane Ashby Hotel, Perth
Dress: Formal
The evening will include drinks, a three-course dinner, music and dancing.
Ticket price $139, on sale now! To purchase tickets go to:
(website to be announced)
Proceeds go to Makers Across Frontiers
is is an 18+ event. Open to general public.
Nice to have
• Modern, Classy, Similar to previous years designs. Possibly Masquerade themed.
Should not have
• Fish, environmental theme, rural Australia theme (these have been done)

```html
<!DOCTYPE html>
<html lang="en">
<head>
<meta charset="utf-8">
<title>Bright Builders WA Ball 2013</title>
<link href="https://fonts.googleapis.com/css2?family=Jost:wght@800&family=Didact+Gothic&display=swap" rel="stylesheet">
<style>
  :root {
    --bg: #000000;
    --white: #ffffff;
    --violet: #8d7fe0;
    --gear-blue: #2c3fd8;
    --gear-cyan: #4f8ff0;
    --gear-violet: #7a4fd0;
    --gear-rust: #c0502a;
    --band: rgba(30, 40, 70, 0.55);
  }
  * { margin: 0; padding: 0; box-sizing: border-box; }
  html, body {
    width: 854px; height: 1200px; overflow: hidden; background: var(--bg);
  }
  .poster {
    position: relative; width: 854px; height: 1200px; overflow: hidden;
    background: var(--bg); color: var(--white); text-align: center;
    font-family: "Didact Gothic", sans-serif;
  }
  .gear-art {
    position: absolute; left: 0; top: 530px; width: 854px; height: 670px;
    background:
      radial-gradient(ellipse 170px 150px at 300px 120px, rgba(70,90,255,0.75), transparent 70%),
      radial-gradient(ellipse 200px 160px at 460px 310px, rgba(150,90,230,0.7), transparent 70%),
      radial-gradient(ellipse 150px 130px at 160px 260px, rgba(200,90,50,0.55), transparent 70%),
      radial-gradient(ellipse 220px 200px at 680px 480px, rgba(60,120,240,0.6), transparent 70%),
      radial-gradient(ellipse 260px 200px at 200px 560px, rgba(50,80,230,0.7), transparent 70%),
      radial-gradient(ellipse 520px 420px at 420px 380px, rgba(40,50,160,0.6), transparent 75%);
  }
  .intro {
    position: absolute; top: 28px; width: 100%;
    color: var(--violet); font-size: 23px;
  }
  .title {
    position: absolute; top: 92px; width: 100%;
    font-family: "Jost", sans-serif; font-weight: 800;
    font-size: 49px; line-height: 68px; letter-spacing: 0.5px;
  }
  .subtitle {
    position: absolute; top: 232px; width: 100%;
    color: var(--violet); font-size: 28px;
  }
  .when {
    position: absolute; top: 292px; width: 100%;
    font-family: "Jost", sans-serif; font-weight: 800;
    font-size: 42px; line-height: 58px;
  }
  .programme {
    position: absolute; top: 424px; width: 100%;
    color: var(--violet); font-size: 24px; line-height: 35px;
  }
  .ticket-badge {
    position: absolute; left: 592px; top: 548px; width: 230px; height: 230px;
    border-radius: 50%; background: var(--bg); border: 6px solid var(--white);
    display: flex; flex-direction: column; justify-content: center; align-items: center;
    transform: rotate(12deg);
  }
  .ticket-badge .label { font-size: 29px; line-height: 36px; }
  .ticket-badge .price {
    font-family: "Jost", sans-serif; font-weight: 800; font-size: 40px; line-height: 52px;
  }
  .details {
    position: absolute; top: 858px; width: 100%;
    font-size: 37px; line-height: 55px;
  }
  .footer-band {
    position: absolute; left: 0; top: 1075px; width: 854px; height: 125px;
    background: var(--band);
    font-size: 27px; line-height: 34px; padding-top: 10px;
  }
</style>
</head>
<body>
  <main class="poster">
    <div class="gear-art" role="img" aria-label="Cluster of glowing blue, violet and copper machine gears"></div>

    <p class="intro">Join us in celebrating the</p>
    <h1 class="title">Annual Bright Builders<br>of Western Australia Ball</h1>
    <p class="subtitle">with a night of dinner and entertainment</p>
    <p class="when">Saturday July 13th, 2013<br>Time: 7pm Arrival</p>
    <p class="programme">The evening will include drinks, a three-course<br>dinner, music and dancing.</p>

    <div class="ticket-badge">
      <span class="label">Ticket price</span>
      <span class="price">$139</span>
      <span class="label">on sale now!</span>
    </div>

    <p class="details">
      Venue: Corvane Ashby Hotel, Perth<br>
      Dress: Formal<br>
      To purchase tickets go to:<br>
      (website to be announced)
    </p>

    <footer class="footer-band">
      Proceeds go to Makers Across Frontiers<br>
      This is an 18+ event. Open to general public.
    </footer>
  </main>
</body>
</html>
```